Brightleaf Homes needs a web design and brand identifier

Brightleaf Homes is a pioneering approach by Victorian councils and four greenhouse alliances to support low income households to install solar systems with no upfront costs.

Brightleaf Homes will commence in May 2017.

Brightleaf Homes is looking for a designer to create a website banner incorporating a brand identifier for Brightleaf Homes. The brand identifier will be used in Brightleaf Homes promotional materials, such as flyers and mail outs.

The website banner and brand identifier should engender trust and confidence in the target group (retirees).
Updates

Project Deadline Extended
Reason: Hi, Thank you for your work so far. We've been given advice to get a separate logo designed (instead of trying to include this as part of the banner design). Sorry for not realising this until now - we're new to all this. So, I have a couple of preliminary logo designs that are being considered by our project control group. I will forward a copy of the logo once we have it. The project control group is looking for a web design that is unique to Brightleaf Homes and a design that draws on the key elements of the program (i.e. it helps people save money and take control). The site should be friendly but not too informal as the target group is seniors. Here's a link to another community energy organisation: www.kelvowattgroup.com.au/ Apologies again for the delays. Cheers, Tomas

Target Market(s)

Home owning, low income, retirees

Industry/Entity Type

Non Profit

Number of Pages Required

1 page

Font styles to use
Sans Serif

Requirements
Must have
• Use of Brightleaf Home name
• Must promote Brightleaf Homes as safe, reliable and trustworthy
Nice to have
• Blue - to engender sense of safety and confidence (open to suggestions, though)
• Solar panels / the sun
Should not have
• Anything that is hard to read
• anything that promotes riskyness

```html
<!DOCTYPE html>
<html lang="en">
<head>
<meta charset="utf-8">
<title>Brightleaf Homes</title>
<link href="https://fonts.googleapis.com/css2?family=Lato:wght@300;400;700;900&display=swap" rel="stylesheet">
<style>
:root{
  --green:#6a9a3c;
  --green-dark:#5a8731;
  --orange:#f0b233;
  --cream:#fdf8e6;
  --ink:#2b2b2b;
  --text:#555;
  --muted:#8a8a8a;
  --olive:#5c5a45;
  --white:#fff;
  --line:#e6e1cf;
}
*{box-sizing:border-box;margin:0;padding:0}
html,body{width:1200px;height:3805px;overflow:hidden}
body{position:relative;font-family:'Lato',sans-serif;color:var(--text);background:var(--white);font-size:14px;line-height:1.6}
.sec{position:absolute;left:0;width:1200px}
a{color:inherit;text-decoration:none}

/* top bar */
.topbar{top:0;height:35px;background:var(--cream);border-bottom:1px solid var(--line);font-size:13px;color:var(--ink)}
.topbar .social{position:absolute;left:81px;top:12px;display:flex;gap:8px}
.dot{width:10px;height:10px;border-radius:50%;background:#666;display:block}
.topbar .contacts{position:absolute;right:81px;top:7px;display:flex;gap:28px}
.topbar .contacts span{display:flex;align-items:center;gap:6px}

/* header */
.header{top:35px;height:135px;background:var(--cream)}
.brand{position:absolute;left:50%;top:46px;transform:translateX(-50%);display:flex;align-items:center;gap:14px;color:var(--olive);white-space:nowrap}
.brand-mark{width:38px;height:38px;border-radius:50%;background:var(--green);flex:none}
.brand-name{font-weight:400;font-size:38px;line-height:1}

/* hero */
.hero{top:170px;height:407px;background:linear-gradient(120deg,#2c3440 0%,#48505a 35%,#6b5a4a 60%,#3a4655 100%)}
.hero .photo{position:absolute;inset:0}
.nav{position:absolute;left:81px;top:0;width:1041px;height:38px;background:var(--orange);display:flex;align-items:center;padding-left:25px;color:var(--white);font-size:14px}
.nav a{margin-right:56px}
.nav .search{position:absolute;right:10px;top:8px;width:175px;height:22px;border-bottom:1px solid rgba(255,255,255,.7);font-size:12px;color:rgba(255,255,255,.8);padding-left:4px}
.hero-copy{position:absolute;left:0;width:1200px;top:128px;text-align:center;color:var(--white)}
.hero-copy .kicker{font-size:19px}
.hero-copy h1{font-size:34px;font-weight:700;margin-top:8px}
.point{display:flex;align-items:center;gap:12px;position:absolute;color:var(--white);font-size:16px}
.num{width:36px;height:36px;border-radius:50%;background:var(--white);color:var(--orange);font-weight:700;font-size:18px;display:flex;align-items:center;justify-content:center}
.btn{display:inline-block;color:var(--white);font-weight:700;font-size:13px;text-transform:uppercase;letter-spacing:.5px;text-align:center}
.btn-green{background:var(--green)}
.btn-orange{background:var(--orange)}
.hero .btn{position:absolute;left:501px;top:305px;width:193px;height:43px;line-height:43px}

/* intro */
.intro{top:577px;height:423px;background:var(--cream)}
.intro .eyebrow{position:absolute;left:81px;top:50px;font-size:16px;color:var(--text)}
.intro h2{position:absolute;left:81px;top:78px;width:520px;font-size:31px;line-height:1.35;color:var(--ink);font-weight:700}
.intro .lead{position:absolute;left:81px;top:184px;width:510px;font-size:13px;line-height:1.75;color:var(--muted)}
.intro .btn{position:absolute;left:81px;top:327px;width:193px;height:42px;line-height:42px}
.feature{position:absolute;left:640px;width:500px}
.feature .badge{position:absolute;left:0;top:4px;width:76px;height:76px}
.feature h3{position:absolute;left:84px;top:0;font-size:14px;font-weight:400;text-transform:uppercase;color:var(--text)}
.feature p{position:absolute;left:84px;top:22px;width:400px;font-size:13px;color:var(--muted);line-height:1.7}

/* how it works */
.how{top:1000px;height:519px;background:var(--white)}
.how h2{position:absolute;top:40px;width:1200px;text-align:center;font-size:31px;font-weight:700;color:var(--ink)}
.step{position:absolute;width:400px}
.step .icon{position:absolute;left:0;top:0;width:44px;height:44px}
.step .big{position:absolute;top:-8px;font-size:130px;font-weight:900;color:#eeeeee;line-height:1}
.step p{position:absolute;left:0;top:64px;width:290px;font-size:13px;color:var(--text);line-height:1.7}
.how .rule{position:absolute;height:1px;background:#ececec;top:304px}
.how .diamond{position:absolute;left:435px;top:164px;width:330px;height:330px}

/* landscape */
.landscape{top:1519px;height:279px;background:linear-gradient(180deg,#e1f0f6 0%,#d5eaf3 55%,#b9d98d 78%,#9cc66a 100%)}

/* streams */
.streams{top:1798px;height:574px;background:var(--cream)}
.streams h2{position:absolute;top:40px;width:1200px;text-align:center;font-size:30px;font-weight:700;color:var(--olive)}
.streams svg{position:absolute;left:0;top:0}

/* clients */
.clients{top:2372px;height:216px;background:linear-gradient(180deg,#f3bd3b,#ecaa2a)}
.clients h2{position:absolute;top:16px;width:1200px;text-align:center;font-size:30px;font-weight:700;color:var(--white)}
.client-row{position:absolute;left:75px;top:102px;width:1050px;display:flex;justify-content:space-between}
.client{width:112px;height:86px;background:var(--white);display:flex;align-items:center;justify-content:center;text-align:center;font-size:13px;font-weight:700;color:var(--green-dark);line-height:1.25;padding:6px}

/* news */
.news{top:2588px;height:501px;background:var(--white)}
.news h2{position:absolute;top:50px;width:1200px;text-align:center;font-size:31px;font-weight:700;color:var(--olive)}
.card{position:absolute;top:134px;width:302px}
.card .thumb{width:302px;height:160px}
.card h3{margin-top:18px;font-size:14px;font-weight:700;color:var(--ink);line-height:1.5}
.card p{margin-top:12px;font-size:13px;color:var(--text);line-height:1.6}
.card .more{display:block;margin-top:6px;font-size:13px;color:var(--orange)}

/* call to action */
.cta{top:3089px;height:324px;background:linear-gradient(120deg,#3b4452,#6a6d70 50%,#8b8f92)}
.cta svg{position:absolute;left:0;top:0}
.cta h2{position:absolute;left:625px;top:50px;font-size:31px;font-weight:700;color:var(--white)}
.cta .phone{position:absolute;left:625px;top:110px;font-size:42px;font-weight:300;color:var(--white);letter-spacing:1px}
.cta .or{position:absolute;left:625px;top:166px;font-size:26px;font-weight:300;color:var(--white)}
.cta .btn{position:absolute;left:625px;top:228px;width:195px;height:43px;line-height:43px}

/* footer */
.footer{top:3413px;height:322px;background:var(--cream);border-top:1px solid var(--line)}
.footer .brand{left:81px;top:62px;transform:none;gap:10px}
.footer .brand-name{font-size:24px}
.footer .brand-mark{width:26px;height:26px}
.footer .about{position:absolute;left:81px;top:140px;width:260px;font-size:13px;color:var(--text)}
.footer .fphone{position:absolute;left:81px;top:208px;font-size:22px;font-weight:700;color:var(--ink)}
.fcol{position:absolute;top:55px}
.fcol h4{font-size:13px;font-weight:400;text-transform:uppercase;letter-spacing:1px;color:var(--text);margin-bottom:26px}
.fcol ul{list-style:none;font-size:13px;color:var(--text);line-height:1.6}
.fcol dl{display:grid;grid-template-columns:76px 200px;font-size:13px;row-gap:14px;line-height:1.5}
.fcol .social{display:flex;gap:34px;margin-top:4px}
.fcol .chat{display:flex;align-items:center;gap:16px;margin-top:22px;font-size:13px}
.legal{top:3735px;height:70px;background:var(--cream);border-top:1px solid var(--line);font-size:12px;color:var(--text)}
.legal .copy{position:absolute;left:81px;top:26px}
.legal .terms{position:absolute;right:81px;top:26px}
</style>
</head>
<body>

<div class="sec topbar">
  <div class="social"><span class="dot"></span><span class="dot"></span><span class="dot"></span><span class="dot"></span></div>
  <div class="contacts">
    <span><svg width="9" height="14" viewBox="0 0 9 14"><rect x="0.5" y="0.5" width="8" height="13" rx="1.5" fill="none" stroke="#333"/><circle cx="4.5" cy="11" r="0.9" fill="#333"/></svg>0400 512 367</span>
    <span><svg width="14" height="10" viewBox="0 0 14 10"><rect width="14" height="10" fill="#333"/><path d="M0 0 L7 6 L14 0" fill="none" stroke="#fff"/></svg>tomas.reid[at]hollowvale.vic.gov.au</span>
  </div>
</div>

<header class="sec header">
  <div class="brand">
    <span class="brand-name">Riverbend Alliance</span>
    <span class="brand-mark"></span>
  </div>
</header>

<section class="sec hero">
  <div class="photo" role="img" aria-label="Photo of a tiled house roof fitted with solar panels under a dusky sky"></div>
  <nav class="nav">
    <a>Home</a><a>About</a><a>News</a><a>Projects</a><a>Advocacy</a><a>Resources</a><a>Contact</a>
    <div class="search">Search</div>
  </nav>
  <div class="hero-copy">
    <div class="kicker">With Best quality solar system</div>
    <h1>households to save money and take control of their energy bills</h1>
  </div>
  <div class="point" style="left:245px;top:245px"><span class="num">1</span><span>Affordable.</span></div>
  <div class="point" style="left:490px;top:245px"><span class="num">2</span><span>Quality solar systems</span></div>
  <div class="point" style="left:768px;top:245px"><span class="num">3</span><span>No upfront costs.</span></div>
  <a class="btn btn-green">Get Free Quote</a>
</section>

<section class="sec intro">
  <div class="eyebrow">Solar Enterprise</div>
  <h2>The Energy That is Sourceable free and Healthy</h2>
  <p class="lead">Sed ut perspiciatis unde omnis iste natus error sit voluptatem accusantium doloremque laudantium, totam rem aperiam, eaque ipsa quae ab illo inventore veritatis et quasi architecto beatae vitae dicta sunt explicabo. Nemo enim ipsam voluptatem quia voluptas sit aspernatur aut odit aut fugit, sed quia consequuntur magni dolores eos qui ratione voluptatem sequi nesciunt.</p>
  <a class="btn btn-green">Know More</a>

  <div class="feature" style="top:66px">
    <svg class="badge" viewBox="0 0 76 76"><rect x="15" y="15" width="46" height="46" rx="8" transform="rotate(45 38 38)" fill="var(--orange)"/><path d="M30 30 h16 v10 l-8 8 l-8 -8 z" fill="#fff"/></svg>
    <h3>Safe</h3>
    <p>Sed ut perspiciatis unde omnis iste natus error sit voluptatem accusantium doloremque laudantium.</p>
  </div>
  <div class="feature" style="top:176px">
    <svg class="badge" viewBox="0 0 76 76"><rect x="15" y="15" width="46" height="46" rx="8" transform="rotate(45 38 38)" fill="var(--orange)"/><path d="M28 36 h6 v14 h-6 z M36 36 l6 -9 c2 0 3 2 2 5 h7 c2 0 3 2 2 4 l-3 12 c-1 2 -2 2 -4 2 h-10 z" fill="#fff"/></svg>
    <h3>Reliable</h3>
    <p>Sed ut perspiciatis unde omnis iste natus error sit voluptatem accusantium doloremque laudantium.</p>
  </div>
  <div class="feature" style="top:275px">
    <svg class="badge" viewBox="0 0 76 76"><rect x="15" y="15" width="46" height="46" rx="8" transform="rotate(45 38 38)" fill="var(--orange)"/><circle cx="38" cy="35" r="10" fill="none" stroke="#fff" stroke-width="3"/><path d="M32 43 l-3 11 l5 -3 l3 4 M44 43 l3 11 l-5 -3 l-3 4" fill="none" stroke="#fff" stroke-width="2"/></svg>
    <h3>Quality</h3>
    <p>Sed ut perspiciatis unde omnis iste natus error sit voluptatem accusantium doloremque laudantium.</p>
  </div>
</section>

<section class="sec how">
  <h2>How It Work</h2>

  <div class="step" style="left:81px;top:140px">
    <svg class="icon" viewBox="0 0 44 44"><rect x="4" y="8" width="36" height="20" fill="none" stroke="var(--green)" stroke-width="2"/><path d="M4 18 h36 M13 8 v20 M22 8 v20 M31 8 v20 M12 28 l-4 10 M32 28 l4 10" stroke="var(--green)" stroke-width="2" fill="none"/></svg>
    <span class="big" style="left:210px">1</span>
    <p>Brightleaf Homes checks that every person gets a solar system that pays for itself in energy savings from day one</p>
  </div>
  <div class="step" style="left:81px;top:340px">
    <svg class="icon" viewBox="0 0 44 44"><circle cx="22" cy="18" r="7" fill="none" stroke="var(--green)" stroke-width="5" stroke-dasharray="4 2.5"/><circle cx="22" cy="18" r="3" fill="var(--green)"/><path d="M6 32 h32 v6 h-32 z" fill="var(--green)"/></svg>
    <span class="big" style="left:210px">2</span>
    <p>Brightleaf Homes organises for the solar system to be installed</p>
  </div>
  <div class="step" style="left:815px;top:140px">
    <svg class="icon" viewBox="0 0 44 44"><circle cx="22" cy="13" r="8" fill="none" stroke="var(--green)" stroke-width="2"/><path d="M8 40 c0 -10 6 -15 14 -15 c8 0 14 5 14 15 z" fill="var(--green)"/></svg>
    <span class="big" style="left:235px">3</span>
    <p>Brightleaf Homes supports pensioners to understand and get the most out of solar</p>
  </div>
  <div class="step" style="left:815px;top:340px">
    <svg class="icon" viewBox="0 0 44 44"><circle cx="28" cy="12" r="7" fill="none" stroke="var(--green)" stroke-width="2"/><text x="28" y="16" text-anchor="middle" font-size="10" font-weight="700" fill="var(--green)" font-family="Lato,sans-serif">$</text><path d="M4 30 h10 l8 -4 h10 c2 0 2 4 0 4 h-10 M4 38 h20 l14 -8" fill="none" stroke="var(--green)" stroke-width="2"/></svg>
    <span class="big" style="left:235px">4</span>
    <p>Pensioners gradually pay for cost through their usual rates payments at 0% interest</p>
  </div>

  <div class="rule" style="left:81px;width:330px"></div>
  <div class="rule" style="left:790px;width:330px"></div>

  <svg class="diamond" viewBox="0 0 330 330">
    <defs><linearGradient id="sky" x1="0" y1="0" x2="0" y2="1"><stop offset="0" stop-color="#5a9ad8"/><stop offset="0.55" stop-color="#2f5f9c"/><stop offset="1" stop-color="#8a6a4a"/></linearGradient></defs>
    <rect x="55" y="55" width="220" height="220" rx="26" transform="rotate(45 165 165)" fill="var(--orange)"/>
    <rect x="67" y="67" width="196" height="196" rx="20" transform="rotate(45 165 165)" fill="#fff"/>
    <rect x="73" y="73" width="184" height="184" rx="18" transform="rotate(45 165 165)" fill="url(#sky)" role="img" aria-label="Photo of solar panels on a roof against a blue sky"/>
  </svg>
</section>

<section class="sec landscape" role="img" aria-label="Illustration of wind turbines, trees and solar panels on green hills under a pale sky"></section>

<section class="sec streams">
  <h2>Councils can choose to offer one (or both) of the following streams</h2>
  <svg width="1200" height="574" viewBox="0 0 1200 574">
    <defs>
      <marker id="arrow" viewBox="0 0 10 10" refX="8" refY="5" markerWidth="8" markerHeight="8" orient="auto"><path d="M0 0 L10 5 L0 10 z" fill="#222"/></marker>
      <g id="node"><rect x="-40" y="-40" width="80" height="80" rx="6" transform="rotate(45)" fill="var(--green)"/></g>
    </defs>
    <line x1="600" y1="150" x2="600" y2="520" stroke="#d6d0bb" stroke-width="2"/>

    <g fill="none" stroke="#222" stroke-width="2" marker-end="url(#arrow)">
      <path d="M345 165 Q410 145 440 190"/>
      <path d="M515 290 Q545 325 515 360"/>
      <path d="M440 455 Q395 495 335 470"/>
      <path d="M215 440 Q165 430 160 370"/>
      <path d="M160 250 Q175 195 225 180"/>
      <g transform="translate(548 0)">
        <path d="M345 165 Q410 145 440 190"/>
        <path d="M515 290 Q545 325 515 360"/>
        <path d="M440 455 Q395 495 335 470"/>
        <path d="M215 440 Q165 430 160 370"/>
        <path d="M160 250 Q175 195 225 180"/>
      </g>
    </g>

    <g font-family="Lato,sans-serif" font-weight="700" font-size="13" fill="#fff" text-anchor="middle">
      <g transform="translate(286 190)"><use href="#node"/><circle cx="0" cy="2" r="16" fill="#fff"/><text y="8" font-size="18" fill="var(--green)">$</text></g>
      <g transform="translate(481 235)"><use href="#node"/><circle cx="0" cy="-12" r="9" fill="#fff"/><text y="20">Supplier</text></g>
      <g transform="translate(486 412)"><use href="#node"/><path d="M-20 2 L0 -18 L20 2 M-13 -4 v20 h26 v-20" fill="#fff" stroke="#fff"/><rect x="-5" y="4" width="10" height="12" fill="var(--green)"/></g>
      <g transform="translate(273 450)"><use href="#node"/><text y="-8">Rates</text><text y="8">Notice</text><text y="24">$</text></g>
      <g transform="translate(139 309)"><use href="#node"/><rect x="-16" y="-20" width="32" height="18" fill="#fff"/><text y="18">Council</text></g>
      <text x="355" y="316" fill="var(--ink)" font-weight="400" font-size="16">Council Rates Stream</text>

      <g transform="translate(836 190)"><use href="#node"/><circle cx="0" cy="2" r="16" fill="#fff"/><text y="8" font-size="18" fill="var(--green)">$</text></g>
      <g transform="translate(1025 235)"><use href="#node"/><circle cx="0" cy="-12" r="9" fill="#fff"/><text y="20">Supplier</text></g>
      <g transform="translate(1028 412)"><use href="#node"/><path d="M-20 2 L0 -18 L20 2 M-13 -4 v20 h26 v-20" fill="#fff" stroke="#fff"/><rect x="-5" y="4" width="10" height="12" fill="var(--green)"/></g>
      <g transform="translate(836 450)"><use href="#node"/><text y="-8">Rates</text><text y="8">Notice</text><text y="24">$</text></g>
      <g transform="translate(687 309)"><use href="#node"/><circle cx="0" cy="-12" r="8" fill="#fff"/><text y="18">Lender</text></g>
      <text x="896" y="318" fill="var(--ink)" font-weight="400" font-size="16">Private Low interest</text>
      <text x="896" y="342" fill="var(--ink)" font-weight="400" font-size="16">Finance Stream</text>
    </g>
  </svg>
</section>

<section class="sec clients">
  <h2>Some Of Our Clients</h2>
  <div class="client-row">
    <div class="client">Eastvale</div>
    <div class="client">Ashgrove</div>
    <div class="client">City of Pinecrest</div>
    <div class="client">Bluegum Ranges Council</div>
    <div class="client">Hollowvale</div>
    <div class="client">City of Kestrel</div>
    <div class="client">Lyndale City Council</div>
  </div>
</section>

<section class="sec news">
  <h2>News</h2>
  <article class="card" style="left:81px">
    <div class="thumb" role="img" aria-label="Photo of award winners posing on stage" style="background:linear-gradient(180deg,#e8e8e8,#9a8c84)"></div>
    <h3>Riverbend Wins Regional Green Leadership Award! (Oct 2016)</h3>
    <p>Riverbend continued it's winning streak at this year's Regional Green Leadership Awards, with the Wildlife Watch Eastern Valleys</p>
    <a class="more">Read More</a>
  </article>
  <article class="card" style="left:446px">
    <div class="thumb" role="img" aria-label="Green award certificate graphic for environment day awards" style="background:linear-gradient(180deg,#eef3e6,#a9c97a)"></div>
    <h3>Riverbend Wins Global Green Award! (June 2016)</h3>
    <p>Riverbend continued it's winning streak at this year's Regional Green Leadership Awards, with the Wildlife Watch Eastern Valleys</p>
    <a class="more">Read More</a>
  </article>
  <article class="card" style="left:815px">
    <div class="thumb" role="img" aria-label="Photo of presenters at an awards ceremony with a blue backdrop" style="background:linear-gradient(180deg,#1e3a7a,#2a2a3a)"></div>
    <h3>Riverbend secures millions in savings for councils (June 2016)</h3>
    <p>Riverbend continued it's winning streak at this year's Regional Green Leadership Awards, with the Wildlife Watch Eastern Valleys</p>
    <a class="more">Read More</a>
  </article>
</section>

<section class="sec cta" role="img" aria-label="Photo of a house roof with solar panels">
  <svg width="1200" height="324" viewBox="0 0 1200 324"><polygon points="608,0 1200,0 1200,324 608,324 519,162" fill="var(--green)"/></svg>
  <h2>Call The very Best Professionals</h2>
  <div class="phone">0400 512 367</div>
  <div class="or">Or</div>
  <a class="btn btn-orange">Chat With Us</a>
</section>

<footer class="sec footer">
  <div class="brand">
    <span class="brand-name">Riverbend Alliance</span>
    <span class="brand-mark"></span>
  </div>
  <p class="about">Sed ut perspiciatis unde omnis iste natus error sit accusantium doloremque totam rem aperiam.</p>
  <div class="fphone">0400 512 367</div>

  <div class="fcol" style="left:430px">
    <h4>Quick Link</h4>
    <ul><li>Home</li><li>About</li><li>News</li><li>Projects</li><li>Advocacy</li><li>Resources</li><li>Contact</li></ul>
  </div>
  <div class="fcol" style="left:610px">
    <h4>Contact Us</h4>
    <dl>
      <dt>Address</dt><dd>Riverbend Alliance for Greenhouse Action<br>Hollowvale City Council<br>Wattle Ave, Fernbridge</dd>
      <dt>Email</dt><dd>tomas.reid[at]hollowvale.vic.gov.au</dd>
    </dl>
  </div>
  <div class="fcol" style="left:970px">
    <h4>Follow Us</h4>
    <div class="social"><span class="dot"></span><span class="dot"></span><span class="dot"></span><span class="dot"></span></div>
    <div class="chat"><svg width="20" height="16" viewBox="0 0 20 16"><path d="M2 1 h12 v8 h-7 l-4 3 v-3 h-1 z M15 5 h3 v8 h-1 v3 l-4 -3 h-5 v-2" fill="#555"/></svg>Live Chat With Us</div>
  </div>
</footer>

<div class="sec legal">
  <span class="copy">Copyright © 2017 all right reserved</span>
  <span class="terms">Term &amp; Conditions</span>
</div>

</body>
</html>
```